Business card design needed

Family General Practitioner/ Family Physician.
Logo is the logo of the Crestmoor Guild of Family Clinicians Australia
http://kvplm.tarevo.edu.au/PictureGallery/logos/pages/CGFC%20logo_jpg.htm

Reason: Just a bit more time to make changes and the weekend for me to look at things closely and to choose. Thanks, Lumi

Thanks for all the submissions. So many of them are really works of art. Not one of them are not good. The ones that I am eliminating are the ones that I think are not suitable for me personally only, and because if I don't, it makes it very difficult to decide as many of you are also sending me slight variations of a card. I have just decided to choose a second place card too. Can't thank you all enough. Good luck, Lumi. P.S - Working today till 10 pm as the card says :-), so probably won't be able to give a feedback till late Saturday night or Sunday morning here in Sydney, Australia. 

Reason: Just added a second place to the budget and realised that Australia is ahead of the rest of the world in the time zone (only :-) - don't want to offend anyone or start a debate!! ) , so Monday deadline will mean it will be a weekend for the rest of the world. Just wanted to give everyone more time to submit their best, especially since I will be picking a second card too. Can't thank everyone enough for the submissions. P.S - Not keen on photos on the card.

Contact Information for Business Card

Dr. Lumi Harcourt M.B.B.S., F.C.G.F.C
Family General Practitioner
Address, timings, phone and fax number on the back.

Requirements
Must have
• Timings
Mon 7 am - 7 pm
Tues 7 am - 12 pm
Wed 7 am - 10 pm
Thurs 7 am - 12 pm
Fri 7 am - 8 pm
Sat 8 am - 10 pm
Sun - Off

```html
<!DOCTYPE html>
<html lang="en">
<head>
<meta charset="utf-8">
<title>Dr. Lumi Harcourt – Business Card</title>
<link rel="stylesheet" href="https://fonts.googleapis.com/css2?family=Syncopate:wght@400;700&display=swap">
<style>
  :root {
    --ink: #050505;
    --stripe: #262626;
    --top-band-a: #8c8c8c;
    --top-band-b: #4a4a4a;
    --accent-bar: #a7a7a7;
    --crest-panel: rgba(210, 210, 210, 0.55);
    --text: #ffffff;
    --mark: #3a3a3a;
  }
  html, body {
    margin: 0;
    padding: 0;
    width: 1200px;
    height: 651px;
    overflow: hidden;
    background: var(--ink);
  }
  .card {
    position: relative;
    width: 1200px;
    height: 651px;
    overflow: hidden;
    background:
      repeating-linear-gradient(to bottom,
        var(--stripe) 0px, var(--stripe) 19px,
        var(--ink) 19px, var(--ink) 38px);
    background-position: 0 32px;
    background-color: var(--ink);
    font-family: "Syncopate", sans-serif;
  }
  .top-band {
    position: absolute;
    left: 0; top: 0;
    width: 100%;
    height: 32px;
    background: linear-gradient(to bottom, var(--top-band-a), var(--top-band-b));
  }
  .accent-bar {
    position: absolute;
    right: 0;
    background: var(--accent-bar);
  }
  .bar-1 { top: 51px;  left: 489px; height: 10px; }
  .bar-2 { top: 74px;  left: 556px; height: 16px; }
  .bar-3 { top: 112px; left: 344px; height: 16px; }
  .bar-4 { top: 148px; left: 898px; height: 22px; }
  .bar-5 { top: 190px; left: 556px; height: 17px; }

  .crest-panel {
    position: absolute;
    left: 1009px; top: 0;
    width: 174px; height: 207px;
    background: var(--crest-panel);
    display: flex;
    flex-direction: column;
    align-items: center;
    justify-content: center;
    gap: 14px;
  }
  .crest-panel .mark-square {
    width: 46px; height: 46px;
    background: var(--mark);
  }
  .crest-panel .mark-name {
    color: var(--mark);
    font-size: 20px;
    font-weight: 700;
    letter-spacing: 3px;
  }

  .identity {
    position: absolute;
    left: 51px;
    top: 428px;
    color: var(--text);
    text-transform: lowercase;
  }
  .identity p { margin: 0; white-space: nowrap; }
  .name {
    font-size: 27px;
    letter-spacing: 3px;
    line-height: 38px;
  }
  .post-nominals {
    font-size: 22px;
    letter-spacing: 4px;
    line-height: 48px;
  }
  .role {
    font-size: 22px;
    letter-spacing: 3px;
    line-height: 44px;
  }
  /* Syncopate sets lowercase as small capitals; capitals stay full height */
  .cap { text-transform: none; }
</style>
</head>
<body>
  <main class="card">
    <div class="top-band"></div>
    <div class="accent-bar bar-1"></div>
    <div class="accent-bar bar-2"></div>
    <div class="accent-bar bar-3"></div>
    <div class="accent-bar bar-4"></div>
    <div class="accent-bar bar-5"></div>

    <div class="crest-panel" aria-label="Crestmoor Guild of Family Clinicians Australia">
      <div class="mark-square"></div>
      <div class="mark-name">CGFC</div>
    </div>

    <section class="identity">
      <p class="name"><span class="cap">D</span>r. <span class="cap">L</span>umi <span class="cap">H</span>arcourt</p>
      <p class="post-nominals cap">M.B.B.S., F.C.G.F.C</p>
      <p class="role"><span class="cap">F</span>amily <span class="cap">G</span>eneral <span class="cap">P</span>ractitioner</p>
    </section>
  </main>
</body>
</html>
```